Customer Dashboard Design for Email Security SaaS

Mailbrook is a commercial email spam filter offered as a SaaS product, built and operated by a small German hosting provider. It protects business email accounts against spam, phishing, scam, and viruses using a multilayer filtering pipeline that combines traditional spam detection with AI-powered classification. The product runs entirely on German infrastructure, ensuring data sovereignty for European customers.

We need a complete redesign of the customer-facing dashboard. This is the web application where paying customers manage their email filtering: view their mail log, check quarantined emails, manage allow/blocklists, configure their settings, and handle their subscription. It is the primary touchpoint between Mailbrook and its customers.

Our customers are system administrators, IT managers at small-to-medium businesses, and operators of small hosting providers. They are technically competent but not designers. They expect professional, efficient tools that respect their time. They typically manage 10–500 email accounts and check the dashboard a few times per week, with heavier use during spam incidents.

We have attached the current mockups which really need to be replaced with something good looking.

Target Market(s)

System administrators, IT managers at small-to-medium businesses, and operators of small hosting providers.

Industry/Entity Type

SaaS

Number of Pages Required

5+ page

```html
<!DOCTYPE html>
<html lang="de">
<head>
<meta charset="utf-8">
<title>Mailbrook – Mail-Log</title>
<link href="https://fonts.googleapis.com/css2?family=Poppins:wght@400;500;600;700&display=swap" rel="stylesheet">
<style>
:root{
  --sidebar:#55514b;
  --page:#f2f2f3;
  --orange:#ef8426;
  --hero:#55514b;
  --filter:#e6ddd4;
  --thead:#b3a290;
  --ink:#2d2a27;
  --muted:#6b655e;
  --line:#dcd6cf;
  --panel:#fffcf7;
  --white:#ffffff;
  --ok-bg:#eef7ec;--ok-bd:#b9dcb3;--ok-fg:#3e7a39;
  --warn-bg:#fff5ea;--warn-bd:#f3c08d;--warn-fg:#ea8a2c;
  --bad-bg:#fdeeee;--bad-bd:#f1b9b9;--bad-fg:#e06b6b;
  --info-bg:#eef4fc;--info-bd:#b9cfee;--info-fg:#4a7fc7;
  --red:#e02020;
}
*{box-sizing:border-box;margin:0;padding:0}
html,body{width:1200px;height:775px;overflow:hidden}
body{font-family:"Poppins",sans-serif;background:var(--page);color:var(--ink);position:relative}
svg{display:block}

/* Sidebar */
.sidebar{position:absolute;left:0;top:0;width:235px;height:775px;background:var(--sidebar);color:var(--white)}
.brand{position:absolute;left:21px;top:30px;display:flex;align-items:center;gap:12px}
.brand-mark{width:37px;height:37px;border-radius:8px;background:#77726b}
.brand-name{font-size:22px;font-weight:600;letter-spacing:.2px}
.nav{position:absolute;left:21px;top:95px;width:191px;list-style:none}
.nav-item{height:33px;display:flex;align-items:center;gap:12px;padding-left:10px;font-size:11px;margin-bottom:5.5px;border-radius:4px;white-space:nowrap}
.nav-item svg{width:16px;height:16px;stroke:#fff;fill:none;stroke-width:1.4}
.nav-item.active{background:var(--orange)}

/* Top bar */
.search{position:absolute;left:541px;top:16px;width:264px;height:29px;border-radius:15px;background:var(--white);display:flex;align-items:center;justify-content:space-between;padding:0 12px 0 14px;font-size:9px;color:var(--muted)}
.search svg{width:12px;height:12px;stroke:#777;fill:none;stroke-width:1.5}
.user{position:absolute;left:815px;top:18px;display:flex;align-items:center;gap:8px;font-size:10px;white-space:nowrap}
.avatar{width:24px;height:24px;border-radius:50%;background:#4a4641;display:flex;align-items:center;justify-content:center}
.avatar svg{width:13px;height:13px;stroke:#fff;fill:none;stroke-width:1.4}
.top-btn{position:absolute;top:16px;height:29px;display:flex;align-items:center;justify-content:center;gap:6px;font-size:10.5px;color:var(--white);border-radius:2px;white-space:nowrap}
.top-btn svg{width:14px;height:14px;stroke:#fff;fill:none;stroke-width:1.4}
.btn-quarantine{left:980px;width:103px;background:var(--orange)}
.btn-maillog{left:1088px;width:91px;background:var(--hero)}

/* Hero */
.hero{position:absolute;left:266px;top:65px;width:913px;height:89px;border-radius:8px;background:var(--hero);color:var(--white)}
.hero-icon{position:absolute;left:21px;top:18px;width:52px;height:52px;border-radius:50%;background:var(--white);display:flex;align-items:center;justify-content:center}
.hero-icon svg{width:28px;height:28px;stroke:#b3a290;fill:none;stroke-width:1.4}
.hero-title{position:absolute;left:84px;top:14px;font-size:32px;font-weight:600;line-height:1.2}
.hero-sub{position:absolute;left:84px;top:57px;font-size:10.8px}
.btn-export{position:absolute;right:22px;top:30px;width:94px;height:29px;border:1px solid #fff;border-radius:2px;display:flex;align-items:center;justify-content:center;gap:6px;font-size:10px}
.btn-export svg{width:12px;height:12px;stroke:#fff;fill:none;stroke-width:1.5}

/* Filters */
.filters{position:absolute;left:266px;top:169px;width:913px;height:57px;border-radius:4px;background:var(--filter)}
.field{position:absolute;top:12px}
.field label{display:block;font-size:8px;color:var(--ink);margin-bottom:2px;white-space:nowrap}
.select{height:20px;background:var(--white);border:1px solid #d8d0c7;border-radius:2px;font-size:7.5px;display:flex;align-items:center;justify-content:space-between;padding:0 6px;color:var(--ink);white-space:nowrap}
.select svg{width:6px;height:6px;stroke:#555;fill:none;stroke-width:1.5}
.text-search{position:absolute;left:400px;top:25px;width:176px;height:20px;background:#fff;border:1px solid #d8d0c7;border-radius:2px;display:flex;align-items:center;gap:5px;padding:0 6px;font-size:7.5px;white-space:nowrap}
.text-search svg{width:9px;height:9px;stroke:#555;fill:none;stroke-width:1.5}
.btn-reset{position:absolute;left:796px;top:25px;width:95px;height:20px;background:#fff;border:1px solid #d8d0c7;border-radius:2px;display:flex;align-items:center;justify-content:center;gap:4px;font-size:7.5px;white-space:nowrap}
.btn-reset svg{width:9px;height:9px;stroke:#555;fill:none;stroke-width:1.3}

/* Table */
.table{position:absolute;left:266px;top:237px;width:913px;background:var(--white);border:1px solid var(--line)}
.row{display:grid;grid-template-columns:35px 130px 135px 130px 143px 91px 67px 164px 1fr;align-items:center;height:31px;font-size:8.8px;border-bottom:1px solid var(--line);white-space:nowrap}
.row.wide{grid-template-columns:35px 130px 135px 130px 179px 86px 52px 122px 1fr}
.row:last-child{border-bottom:none}
.thead{background:var(--thead);color:var(--white);font-size:10px;font-weight:500;height:29px;border-bottom:none}
.chev svg{width:8px;height:8px;margin-left:10px;stroke:#555;fill:none;stroke-width:1.5}
.addr{text-decoration:underline;text-underline-offset:2px}
.c-score{padding-left:5px}
.badge{display:inline-flex;align-items:center;gap:3px;height:19px;padding:0 5px;border:1px solid;border-radius:2px;font-size:7.5px;white-space:nowrap}
.badge svg{width:10px;height:10px;fill:none;stroke:currentColor;stroke-width:1.3}
.b-ham{background:var(--ok-bg);border-color:var(--ok-bd);color:var(--ok-fg)}
.b-spam{background:var(--warn-bg);border-color:var(--warn-bd);color:var(--warn-fg)}
.b-phish{background:var(--bad-bg);border-color:var(--bad-bd);color:var(--bad-fg)}
.b-news{background:var(--info-bg);border-color:var(--info-bd);color:var(--info-fg)}
.b-state{background:var(--ok-bg);border-color:#d3e7cd;color:var(--ok-fg)}
.action{display:flex;align-items:center;gap:10px}
.btn-release{height:20px;padding:0 9px;background:var(--orange);color:#fff;border-radius:2px;font-size:8.5px;font-weight:500;display:flex;align-items:center;white-space:nowrap}
.dots svg{width:4px;height:12px;fill:#555}

/* Expanded details */
.details{position:relative;height:205px;background:var(--panel);border-bottom:1px solid var(--line)}
.det-col{position:absolute;top:18px}
.det-col h3{font-size:10px;font-weight:500;margin-bottom:11px}
.reason{display:flex;gap:10px;height:36px}
.reason svg{width:17px;height:17px;stroke:#b3a290;fill:none;stroke-width:1.1;margin-top:2px;flex:none}
.reason b{display:block;font-size:8.6px;font-weight:600;line-height:12px}
.reason span{display:block;font-size:8.6px;line-height:12px;margin-top:3px;white-space:nowrap}
.hdr{display:grid;grid-template-columns:88px 1fr;font-size:8.6px;line-height:12px;margin-bottom:8.7px;white-space:nowrap}
.hdr dt{font-weight:600}
.fail{color:var(--red)}
</style>
</head>
<body>

<aside class="sidebar">
  <div class="brand"><div class="brand-mark"></div><span class="brand-name">Mailbrook</span></div>
  <ul class="nav">
    <li class="nav-item"><svg viewBox="0 0 16 16"><path d="M2 7.5 8 2l6 5.5M3.5 6.5V14h3v-4h3v4h3V6.5"/></svg>Übersicht</li>
    <li class="nav-item active"><svg viewBox="0 0 16 16"><rect x="1.5" y="3.5" width="13" height="9"/><path d="M1.5 3.5 8 9l6.5-5.5M1.5 12.5 6 8M14.5 12.5 10 8"/></svg>Mail-Log</li>
    <li class="nav-item"><svg viewBox="0 0 16 16"><rect x="1.5" y="3.5" width="13" height="9"/><path d="M1.5 3.5 8 9l6.5-5.5"/></svg>Postfächer</li>
    <li class="nav-item"><svg viewBox="0 0 16 16"><path d="M8 1.5 13.5 3.5v4c0 3.5-2.5 5.8-5.5 7-3-1.2-5.5-3.5-5.5-7v-4z"/><path d="m5.5 8 2 2 3-3.5"/></svg>Allowlist</li>
    <li class="nav-item"><svg viewBox="0 0 16 16"><path d="M8 2 14.5 13.5h-13zM8 6.5v3.5M8 11.5v.5"/></svg>Blocklist</li>
    <li class="nav-item"><svg viewBox="0 0 16 16"><circle cx="8" cy="8" r="2.3"/><path d="M8 1.5v2M8 12.5v2M1.5 8h2M12.5 8h2M3.4 3.4l1.4 1.4M11.2 11.2l1.4 1.4M3.4 12.6l1.4-1.4M11.2 4.8l1.4-1.4"/><circle cx="8" cy="8" r="4.6"/></svg>Einstellungen</li>
    <li class="nav-item"><svg viewBox="0 0 16 16"><path d="M3 1.5h10v13l-2-1.2-1.5 1.2L8 13.3l-1.5 1.2L5 13.3 3 14.5zM5.5 5h5M5.5 7.5h5M5.5 10h3"/></svg>Abrechnung</li>
  </ul>
</aside>

<div class="search">Suchen<svg viewBox="0 0 12 12"><circle cx="5" cy="5" r="3.8"/><path d="m8 8 3 3"/></svg></div>
<div class="user"><div class="avatar"><svg viewBox="0 0 14 14"><circle cx="7" cy="4.5" r="2.8"/><path d="M1.8 13c.6-3 2.6-4.5 5.2-4.5s4.6 1.5 5.2 4.5"/></svg></div>Willkommen zurück, Jan!</div>
<div class="top-btn btn-quarantine"><svg viewBox="0 0 14 14"><rect x="2.5" y="6" width="9" height="7"/><path d="M4.5 6V4a2.5 2.5 0 0 1 5 0v2M7 8.5v2"/></svg>Quarantäne</div>
<div class="top-btn btn-maillog"><svg viewBox="0 0 16 14"><rect x="1.5" y="2" width="13" height="10"/><path d="M1.5 2 8 7.5 14.5 2"/></svg>Mail Log</div>

<section class="hero">
  <div class="hero-icon"><svg viewBox="0 0 28 28"><rect x="4" y="8" width="18" height="13"/><path d="m4 8 9 7 9-7M19 4h5v5M24 4l-6 6M9 24H4v-5M4 24l5-5"/></svg></div>
  <h1 class="hero-title">Mail-Log</h1>
  <p class="hero-sub">Alle verarbeiteten E-Mails im System</p>
  <div class="btn-export">Exportieren<svg viewBox="0 0 12 12"><path d="M6 1v7M3 5.5 6 8.5 9 5.5M1 9v2h10V9"/></svg></div>
</section>

<section class="filters">
  <div class="field" style="left:11px"><label>Verdict</label><div class="select" style="width:61px">Alle<svg viewBox="0 0 6 6"><path d="m1 2 2 2 2-2"/></svg></div></div>
  <div class="field" style="left:89px"><label>Zeitraum</label><div class="select" style="width:77px">Letzte 30 Tage<svg viewBox="0 0 6 6"><path d="m1 2 2 2 2-2"/></svg></div></div>
  <div class="field" style="left:182px"><label>Absender/Empfänger</label><div class="select" style="width:114px">Alle<svg viewBox="0 0 6 6"><path d="m1 2 2 2 2-2"/></svg></div></div>
  <div class="field" style="left:312px"><label>Score</label><div class="select" style="width:72px">Alle<svg viewBox="0 0 6 6"><path d="m1 2 2 2 2-2"/></svg></div></div>
  <div class="text-search"><svg viewBox="0 0 12 12"><circle cx="5" cy="5" r="3.8"/><path d="m8 8 3 3"/></svg>Suche (Betreff, Inhalt, IP...)</div>
  <div class="btn-reset"><svg viewBox="0 0 10 10"><path d="M1 1.5h8L6 5.2V9L4 8V5.2z"/></svg>Filter Zurücksetzen</div>
</section>

<section class="table">
  <div class="row thead"><span></span><span>Zeitstempel</span><span>Absender</span><span>Empfänger</span><span>Betreff</span><span>Verdict</span><span>Score</span><span>Aktion</span><span></span></div>

  <div class="row">
    <span class="chev"><svg viewBox="0 0 8 8"><path d="m2.5 1 3 3-3 3"/></svg></span>
    <span>30. Apr. 2025,&nbsp; 14:32:15</span><span class="addr">invoice@brightledger.org</span><span class="addr">jan@mailbrook.com</span><span>Ihre Rechnung April 2025</span>
    <span><span class="badge b-ham"><svg viewBox="0 0 10 10"><path d="M5 1 8.5 2.3v2.5C8.5 7 7 8.3 5 9 3 8.3 1.5 7 1.5 4.8V2.3z"/><path d="m3.5 5 1 1 2-2"/></svg>Ham</span></span>
    <span class="c-score">98%</span>
    <span><span class="badge b-state">Zugestellt</span></span>
    <span class="dots"><svg viewBox="0 0 4 12"><circle cx="2" cy="2" r="1"/><circle cx="2" cy="6" r="1"/><circle cx="2" cy="10" r="1"/></svg></span>
  </div>

  <div class="row">
    <span class="chev"><svg viewBox="0 0 8 8"><path d="m2.5 1 3 3-3 3"/></svg></span>
    <span>30. Apr. 2025,&nbsp; 14:31:02</span><span class="addr">invoice@brightledger.org</span><span class="addr">jan@mailbrook.com</span><span>50% Rabatt nur heute!</span>
    <span><span class="badge b-spam"><svg viewBox="0 0 10 10"><path d="M5 1 9.3 8.8H.7zM5 4v2.3M5 7.3v.3"/></svg>Spam</span></span>
    <span class="c-score">87%</span>
    <span><span class="badge b-state">In Spam Verschoben</span></span>
    <span class="dots"><svg viewBox="0 0 4 12"><circle cx="2" cy="2" r="1"/><circle cx="2" cy="6" r="1"/><circle cx="2" cy="10" r="1"/></svg></span>
  </div>

  <div class="row">
    <span class="chev"><svg viewBox="0 0 8 8"><path d="m1 2.5 3 3 3-3"/></svg></span>
    <span>30. Apr. 2025,&nbsp; 14:28:47</span><span class="addr">invoice@brightledger.org</span><span class="addr">jan@mailbrook.com</span><span>Unusual sign-in detected</span>
    <span><span class="badge b-phish"><svg viewBox="0 0 10 10"><rect x="1" y="3" width="8" height="6"/><path d="m1 3 4 3 4-3M5 .5v1.5"/></svg>Phishing</span></span>
    <span class="c-score">96%</span>
    <span class="action"><span class="badge b-state">In Quarantäne</span><span class="btn-release">Release Mail</span></span>
    <span class="dots"><svg viewBox="0 0 4 12"><circle cx="2" cy="2" r="1"/><circle cx="2" cy="6" r="1"/><circle cx="2" cy="10" r="1"/></svg></span>
  </div>

  <div class="details">
    <div class="det-col" style="left:19px">
      <h3>Klassifizierungs-Details</h3>
      <div class="reason"><svg viewBox="0 0 18 18"><circle cx="9" cy="9" r="7.5"/><ellipse cx="9" cy="9" rx="3.3" ry="7.5"/><path d="M1.5 9h15M2.6 5h12.8M2.6 13h12.8"/></svg><div><b>Verdächtige Absender-Domain</b><span>Die Domain payvault.com ähnelt bekannten Phishing-Domains.</span></div></div>
      <div class="reason"><svg viewBox="0 0 18 18"><path d="M7.5 10.5 10.5 7.5M6 8.5 4 10.5a2.8 2.8 0 0 0 4 4l2-2M12 9.5l2-2a2.8 2.8 0 0 0-4-4l-2 2M2 3l2 2M13 15l2 2"/></svg><div><b>Auffällige Links</b><span>Enthält 2 verdächtige Links zu nicht vertrauenswürdigen Websites</span></div></div>
      <div class="reason"><svg viewBox="0 0 18 18"><path d="M4.5 15V10a4.5 4.5 0 0 1 9 0v5M3 15h12v1.5H3zM9 1v2M3 3.5l1.3 1.3M15 3.5l-1.3 1.3M1 8h1.8M15.2 8H17"/></svg><div><b>Dringlichkeits-Ton</b><span>Verwendet Sprache, die zu schnellem Handeln auffordert.</span></div></div>
      <div class="reason"><svg viewBox="0 0 18 18"><rect x="1.5" y="2" width="15" height="13"/><path d="M1.5 5h15M4 8h6M4 10.5h4M4 13h3M11 9l4 4-1.8.3-.9 1.6z"/></svg><div><b>HTML-Formular erkannt</b><span>Enthält ein HTML-Formular zum Sammeln von Anmeldedaten.</span></div></div>
    </div>
    <div class="det-col" style="left:455px">
      <h3>Header-Informationen</h3>
      <dl>
        <div class="hdr"><dt>Return-Path:</dt><dd>&lt;security@payvault.com&gt;</dd></div>
        <div class="hdr"><dt>Received:</dt><dd>from shady-relay.net (203.0.113.45)</dd></div>
        <div class="hdr"><dt>IP-Adresse:</dt><dd>203.0.113.45</dd></div>
        <div class="hdr"><dt>SPF:</dt><dd><span class="fail">X</span> Fehlgeschlagen</dd></div>
        <div class="hdr"><dt>DKIM:</dt><dd><span class="fail">X</span> Fehlgeschlagen</dd></div>
        <div class="hdr"><dt>DMARC:</dt><dd><span class="fail">X</span> Fehlgeschlagen</dd></div>
      </dl>
    </div>
  </div>

  <div class="row wide">
    <span class="chev"><svg viewBox="0 0 8 8"><path d="m2.5 1 3 3-3 3"/></svg></span>
    <span>30. Apr. 2025,&nbsp; 14:25:11</span><span>newsletter@technotiz.com</span><span class="addr">jan@mailbrook.com</span><span>TechNotiz: KW 18 – Die besten Stories</span>
    <span><span class="badge b-news"><svg viewBox="0 0 10 10"><path d="M5 1 9.3 8.8H.7zM5 4v2.3M5 7.3v.3"/></svg>Newsletter</span></span>
    <span>95%</span>
    <span><span class="badge b-state">Zugestellt</span></span>
    <span class="dots"><svg viewBox="0 0 4 12"><circle cx="2" cy="2" r="1"/><circle cx="2" cy="6" r="1"/><circle cx="2" cy="10" r="1"/></svg></span>
  </div>

  <div class="row wide">
    <span class="chev"><svg viewBox="0 0 8 8"><path d="m2.5 1 3 3-3 3"/></svg></span>
    <span>30. Apr. 2025,&nbsp; 14:22:33</span><span>ceo@northfield.com</span><span class="addr">jan@mailbrook.com</span><span>Dringend: Bitte um Rückmeldung</span>
    <span><span class="badge b-ham"><svg viewBox="0 0 10 10"><path d="M5 1 8.5 2.3v2.5C8.5 7 7 8.3 5 9 3 8.3 1.5 7 1.5 4.8V2.3z"/><path d="m3.5 5 1 1 2-2"/></svg>Ham</span></span>
    <span>99%</span>
    <span><span class="badge b-state">Zugestellt</span></span>
    <span class="dots"><svg viewBox="0 0 4 12"><circle cx="2" cy="2" r="1"/><circle cx="2" cy="6" r="1"/><circle cx="2" cy="10" r="1"/></svg></span>
  </div>
</section>

</body>
</html>
```